Medical Marijuana Potato Chip Bags Need Graphic Design

We are looking for a bag design for our new brand of medical marijuana potato chips. The design should be simple, the less colors used the better. We are looking for a classic kind of potato chip design somewhere between that of the bag design of Harrow Lane Potato Chips, Brinna's Pita Chips and Fell Ridge Potato Chips.

The main logo is "Toasty Grove Munchies" with "Potato Chips" written underneath it. The original idea was to have a simple sketch of a POTATO SMOKING A JOINT underneath the font, open to other ideas but that would be ideal. In terms of texture and color, we are very open but if you're lost use a burlap sack as influence

This is for the front and back so the design should be able to wrap around. Details such as nutrition info will be added later.
The dimensions are 10"x8" (that includes front and back) or two 5"x8" pictures (one for front, one for back).
Remember that it must appeal to the variety of patients using medical marijuana, from young adults with minor ailments to senior citizens with terminal diseases.

We've decided to make our project non-refundable so the best idea will be rewarded!

Reason: We are just waiting on a few more designs from designers who requested more time. Great job on all the designs so far!

```html
<!DOCTYPE html>
<html lang="en">
<head>
<meta charset="utf-8">
<title>Toasty Grove Munchies – Original Herb Potato Chips Bag Wrap</title>
<link href="https://fonts.googleapis.com/css2?family=Cinzel:wght@400;700;900&display=swap" rel="stylesheet">
<style>
  :root {
    --stage: #000000;
    --cream: #fbf9c4;
    --cream-bright: #fffde0;
    --cream-deep: #f1ec9c;
    --forest: #2f4a1a;
    --forest-deep: #253c14;
    --forest-light: #5f8a2e;
    --leaf: #5b7d27;
    --ink: #223a10;
    --logo-cream: #f3f0b4;
    --stamp-red: #d8232f;
  }
  * { box-sizing: border-box; margin: 0; padding: 0; }
  html, body {
    width: 1200px; height: 900px; overflow: hidden;
    background: var(--stage);
  }
  .canvas {
    position: relative; width: 1200px; height: 900px;
    background: var(--stage);
    font-family: "Cinzel", "Times New Roman", serif;
  }
  .wrap {
    position: absolute; left: 0; top: 210px;
    width: 1200px; height: 480px;
    display: flex;
  }
  .panel {
    position: relative; width: 600px; height: 480px; overflow: hidden;
    background: linear-gradient(90deg,
      var(--cream-deep) 0%, var(--cream) 12%, var(--cream-bright) 45%,
      var(--cream) 80%, var(--cream-deep) 100%);
  }
  .panel__sky {
    position: absolute; left: 0; top: 35px; width: 600px; height: 190px;
    background:
      radial-gradient(ellipse 260px 170px at 150px 100px, var(--forest-light) 0%, #47692a 35%, var(--forest) 70%, var(--forest-deep) 100%);
  }
  .panel__band {
    position: absolute; left: 0; top: 383px; width: 600px; height: 62px;
    background: var(--forest);
  }
  .brand {
    position: absolute; left: 20px; top: 62px; width: 262px;
    text-align: center; color: var(--logo-cream);
  }
  .brand__main {
    font-weight: 700; font-size: 54px; line-height: 60px; letter-spacing: 1px;
  }
  .brand__sub {
    font-weight: 700; font-size: 21px; line-height: 26px; letter-spacing: 0.5px;
  }
  .product-type {
    position: absolute; left: 40px; top: 178px; width: 242px;
    text-align: center; color: var(--logo-cream);
    font-weight: 700; font-size: 15px; letter-spacing: 0.5px;
  }
  .flavour {
    position: absolute; left: 20px; top: 246px; width: 262px;
    text-align: center; color: var(--leaf);
    font-weight: 700; font-size: 36px; line-height: 38px;
  }
  .stamp {
    position: absolute; left: 202px; top: 312px;
    padding: 1px 5px;
    border: 2px solid var(--stamp-red); border-radius: 3px;
    color: var(--stamp-red); font-weight: 700; font-size: 10px; letter-spacing: 0.5px;
    transform: rotate(-20deg);
  }
  .tagline {
    position: absolute; left: 40px; top: 349px; width: 222px;
    text-align: center; color: var(--ink);
    font-size: 11px; letter-spacing: 0.5px;
  }
  .story {
    position: absolute; left: 326px; top: 232px; width: 262px;
    text-align: center; color: var(--ink);
    font-weight: 400; font-size: 10.5px; line-height: 12px; text-transform: uppercase;
  }
  .brand-mini {
    position: absolute; left: 380px; top: 330px; width: 156px;
    text-align: center; color: var(--ink); font-weight: 700;
  }
  .brand-mini__main { font-size: 22px; line-height: 24px; }
  .brand-mini__sub { font-size: 10px; line-height: 12px; }
</style>
</head>
<body>
<main class="canvas">
  <section class="wrap" aria-label="Potato chip bag wrap, front and back">
    <article class="panel">
      <div class="panel__sky" role="img" aria-label="Green sunburst rays behind the brand name"></div>
      <div class="panel__band"></div>
      <div class="brand">
        <div class="brand__main">TOASTY</div>
        <div class="brand__sub">GROVE MUNCHIES</div>
      </div>
      <div class="product-type">POTATO CHIPS</div>
      <h1 class="flavour">ORIGINAL<br>HERB</h1>
      <div class="stamp">MEDICINAL</div>
      <p class="tagline">MUNCH···BUZZ···MUNCH</p>
      <p class="story">Savor the flavour of our delicious holistic chips. We keep you in mind from body to soul. Carefully cooking our potatoes with the finest oils, and then season them to perfection with our freshest sativa and spices for a tasty therapeutic snack.</p>
      <div class="brand-mini">
        <div class="brand-mini__main">TOASTY</div>
        <div class="brand-mini__sub">GROVE MUNCHIES</div>
      </div>
    </article>
    <article class="panel">
      <div class="panel__sky" role="img" aria-label="Green sunburst rays behind the brand name"></div>
      <div class="panel__band"></div>
      <div class="brand">
        <div class="brand__main">TOASTY</div>
        <div class="brand__sub">GROVE MUNCHIES</div>
      </div>
      <div class="product-type">POTATO CHIPS</div>
      <h2 class="flavour">ORIGINAL<br>HERB</h2>
      <div class="stamp">MEDICINAL</div>
      <p class="tagline">MUNCH···BUZZ···MUNCH</p>
      <p class="story">Savor the flavour of our delicious holistic chips. We keep you in mind from body to soul. Carefully cooking our potatoes with the finest oils, and then season them to perfection with our freshest sativa and spices for a tasty therapeutic snack.</p>
      <div class="brand-mini">
        <div class="brand-mini__main">TOASTY</div>
        <div class="brand-mini__sub">GROVE MUNCHIES</div>
      </div>
    </article>
  </section>
</main>
</body>
</html>
```